Evaporative Air Conditioning Summer Service

Would like to design a flyer to send out in an email to existing clients to promote a Pre-summer service for Evaporative Air Conditioners
Cost will be $110.00 inc gst
Tasks included in service are
- Inspection and clean of pads
- Inspection and check float valve, water pump, fan, motor, bearings, drain
- Clean basin
- Supply of bacterial tablet
- Inspect overall condition of unit
- Any repairs if required will be quoted
Please see files attached of a previous very basic flyer I have used for installation and replacement unit costs. This has current contact information
Have also uploaded company logo for use.
Thanks
Plumbing

```html
<!DOCTYPE html>
<html lang="en">
<head>
<meta charset="UTF-8">
<title>Northgate Gas &amp; Plumbing – Pre-Summer Evaporative Service</title>
<link href="https://fonts.googleapis.com/css2?family=Montserrat:wght@400;500;600;700;800&display=swap" rel="stylesheet">
<style>
  :root {
    --sky: #5ab4dc;
    --sky-light: #7cc6e8;
    --sky-deep: #47a9d7;
    --navy: #1f4ea6;
    --green: #1c7a3b;
    --yellow: #f7dc3c;
    --white: #ffffff;
    --ink: #111821;
    --page: #fbfcfd;
    --silver-a: #f1f3f5;
    --silver-b: #d6dbe0;
  }
  * { margin: 0; padding: 0; box-sizing: border-box; }
  html, body { width: 848px; height: 1200px; overflow: hidden; }
  body { font-family: "Montserrat", sans-serif; background: var(--page); }
  .flyer { position: relative; width: 848px; height: 1200px; overflow: hidden; background: var(--page); }

  .header {
    position: absolute; left: 0; top: 0; width: 848px; height: 150px;
    background: linear-gradient(168deg, var(--sky-deep) 0%, var(--sky) 60%, var(--sky-light) 100%);
  }
  .brand { position: absolute; display: flex; align-items: center; gap: 12px; }
  .brand-dot { width: 40px; height: 40px; border-radius: 50%; background: var(--navy); flex: none; }
  .brand-name { font-weight: 800; color: var(--navy); letter-spacing: 1px; white-space: nowrap; }
  .header .brand { left: 0; right: 0; top: 48px; justify-content: center; }
  .header .brand-name { font-size: 42px; }

  .illustration {
    position: absolute; left: 6px; top: 196px; width: 341px; height: 325px;
    background: linear-gradient(180deg, #f4f6f8 0%, #eef1f3 40%, #63bde9 55%, #49aad8 100%);
  }
  .price-badge {
    position: absolute; left: 65px; top: 521px; width: 205px; height: 93px;
    background: linear-gradient(160deg, #6dbee4 0%, #5ab3de 55%, #4aa9d8 100%);
    border-radius: 46px 46px 0 46px;
    text-align: center; padding-top: 4px;
  }
  .price-label { font-size: 36px; font-weight: 700; color: var(--yellow); line-height: 38px; }
  .price-value { font-size: 38px; font-weight: 700; color: var(--white); line-height: 40px; }

  .intro { position: absolute; left: 370px; top: 211px; width: 458px; text-align: center; }
  .intro-title { font-size: 24px; font-weight: 700; color: var(--navy); line-height: 41px; }
  .intro-text { margin-top: 8px; font-size: 18.6px; font-weight: 400; color: var(--green); line-height: 34.5px; }

  .product-frame {
    position: absolute; left: 563px; top: 554px; width: 276px; height: 218px;
    border: 1.5px solid var(--sky-deep);
  }
  .product-photo {
    position: absolute; left: 449px; top: 475px; width: 390px; height: 297px;
    background: radial-gradient(ellipse at 60% 45%, var(--silver-a) 0%, var(--silver-b) 60%, #eef1f3 100%);
    clip-path: polygon(0 0, 100% 0, 100% 100%, 29.5% 100%, 29.5% 72%, 0 72%);
  }

  .services { position: absolute; left: 31px; top: 690px; width: 560px; }
  .services-title { font-size: 22px; font-weight: 700; color: var(--green); margin-bottom: 6px; }
  .service-list { list-style: none; }
  .service-item { position: relative; padding-left: 79px; font-size: 24px; font-weight: 400; color: var(--green); line-height: 37.6px; }
  .service-item svg { position: absolute; left: 1px; top: 6px; width: 30px; height: 24px; }

  .footer {
    position: absolute; left: 0; top: 1044px; width: 848px; height: 156px;
    background: linear-gradient(172deg, var(--sky-deep) 0%, var(--sky) 70%, var(--sky-light) 100%);
    border-bottom: 3px solid var(--yellow);
  }
  .contact-heading {
    position: absolute; left: 0; right: 0; top: 14px; text-align: center;
    font-size: 19px; font-weight: 700; letter-spacing: 2.5px; color: var(--ink);
  }
  .contact-row { position: absolute; left: 44px; display: flex; align-items: center; color: var(--ink); }
  .contact-row svg { flex: none; }
  .contact-phone { top: 56px; font-size: 17px; font-weight: 700; letter-spacing: 2px; gap: 21px; }
  .contact-email { top: 118px; font-size: 16px; font-weight: 400; letter-spacing: 0.5px; gap: 23px; }
  .abn { position: absolute; left: 635px; top: 50px; font-size: 16px; font-weight: 400; color: var(--ink); }
  .footer .brand { right: 10px; top: 84px; gap: 7px; }
  .footer .brand-dot { width: 20px; height: 20px; }
  .footer .brand-name { font-size: 14.5px; letter-spacing: 0; }
</style>
</head>
<body>
<main class="flyer">
  <header class="header">
    <div class="brand">
      <span class="brand-dot"></span>
      <span class="brand-name">NORTHGATE GAS &amp; PLUMBING</span>
    </div>
  </header>

  <div class="illustration" role="img" aria-label="Illustration of a wall-mounted air conditioner blowing cool air over a relaxed man lounging on a bean bag against a blue panel"></div>

  <div class="price-badge">
    <div class="price-label">cost</div>
    <div class="price-value">$110</div>
  </div>

  <section class="intro">
    <h1 class="intro-title">WE PROVIDE MAINTENANCE<br>AND CLEANING SERVICES OF<br>EVAPORATIVE AIR CONDITIONERS</h1>
    <p class="intro-text">BOOK OUR PRE-SUMMER SERVICE PACKAGE<br>AT DISCOUNTED PRICE AND ENJOY<br>THE ALL NEW FRESH AIR.</p>
  </section>

  <div class="product-frame"></div>
  <div class="product-photo" role="img" aria-label="Photo of silver air conditioning units: a window unit, a split system indoor unit, an outdoor condenser and a remote control"></div>

  <section class="services">
    <h2 class="services-title">Services we provide in this package are:</h2>
    <ul class="service-list">
      <li class="service-item"><svg viewBox="0 0 30 24" aria-hidden="true"><path d="M9 20 C14 9 20 3 29 1 C27 10 21 17 12 19 Z" fill="#3fb56a"/><path d="M1 14 L6 21 L28 2" fill="none" stroke="#111" stroke-width="2.4"/></svg>Inspection and clean of pads</li>
      <li class="service-item"><svg viewBox="0 0 30 24" aria-hidden="true"><path d="M9 20 C14 9 20 3 29 1 C27 10 21 17 12 19 Z" fill="#3fb56a"/><path d="M1 14 L6 21 L28 2" fill="none" stroke="#111" stroke-width="2.4"/></svg>Inspection and check float valve, water pump, fan, motor, bearings, drain</li>
      <li class="service-item"><svg viewBox="0 0 30 24" aria-hidden="true"><path d="M9 20 C14 9 20 3 29 1 C27 10 21 17 12 19 Z" fill="#3fb56a"/><path d="M1 14 L6 21 L28 2" fill="none" stroke="#111" stroke-width="2.4"/></svg>Clean basin</li>
      <li class="service-item"><svg viewBox="0 0 30 24" aria-hidden="true"><path d="M9 20 C14 9 20 3 29 1 C27 10 21 17 12 19 Z" fill="#3fb56a"/><path d="M1 14 L6 21 L28 2" fill="none" stroke="#111" stroke-width="2.4"/></svg>Supply of bacterial tablet</li>
      <li class="service-item"><svg viewBox="0 0 30 24" aria-hidden="true"><path d="M9 20 C14 9 20 3 29 1 C27 10 21 17 12 19 Z" fill="#3fb56a"/><path d="M1 14 L6 21 L28 2" fill="none" stroke="#111" stroke-width="2.4"/></svg>Inspect overall condition of unit</li>
      <li class="service-item"><svg viewBox="0 0 30 24" aria-hidden="true"><path d="M9 20 C14 9 20 3 29 1 C27 10 21 17 12 19 Z" fill="#3fb56a"/><path d="M1 14 L6 21 L28 2" fill="none" stroke="#111" stroke-width="2.4"/></svg>Any repairs if required will be quoted</li>
    </ul>
  </section>

  <footer class="footer">
    <div class="contact-heading">-: CONTACT INFO :-</div>
    <div class="contact-row contact-phone">
      <svg width="34" height="34" viewBox="0 0 24 24" aria-hidden="true"><path fill="#fff" d="M6.6 10.8c1.4 2.8 3.8 5.1 6.6 6.6l2.2-2.2c.3-.3.7-.4 1-.2 1.1.4 2.3.6 3.6.6.6 0 1 .4 1 1V20c0 .6-.4 1-1 1C10.6 21 3 13.4 3 4c0-.6.4-1 1-1h3.5c.6 0 1 .4 1 1 0 1.3.2 2.5.6 3.6.1.3 0 .7-.2 1l-2.3 2.2z"/></svg>
      <span>0491570156</span>
    </div>
    <div class="contact-row contact-email">
      <svg width="34" height="25" viewBox="0 0 34 25" aria-hidden="true"><rect x="0" y="0" width="34" height="25" rx="3" fill="#fff"/><path d="M2 3 L17 14 L32 3" fill="none" stroke="#4aaedb" stroke-width="3"/></svg>
      <span>admin@northgategasplumbing.com.au</span>
    </div>
    <div class="abn">ABN - 48120496735</div>
    <div class="brand">
      <span class="brand-dot"></span>
      <span class="brand-name">NORTHGATE GAS &amp; PLUMBING</span>
    </div>
  </footer>
</main>
</body>
</html>
```